need to update our new address on letterhead and business cards. Also open to
a redesign and logo in the near future as we are changing our name. New address is Bramcote Commerce Court, 781 Ashgrove Street, Ashbury, CT 06287

Target Market(s)

35-75 yrs of age

Industry/Entity Type

Business

Requirements
Nice to have
• We are a financial firm so this need to look impressive and classy

```html
<!DOCTYPE html>
<html lang="en">
<head>
<meta charset="utf-8">
<title>Harborline Financial – Stationery Set</title>
<link rel="stylesheet" href="https://fonts.googleapis.com/css2?family=Noto+Serif:wght@400&family=Source+Sans+3:wght@400;600&display=swap">
<style>
  :root {
    --backdrop: #d9d9d9;
    --paper: #ffffff;
    --navy: #0f203f;
    --ink: #1d2533;
    --mist: #c3ccd8;
    --shadow: 0 3px 8px rgba(0,0,0,.22);
  }
  * { box-sizing: border-box; margin: 0; padding: 0; }
  html, body { width: 1200px; height: 1200px; overflow: hidden; }
  body { background: var(--backdrop); font-family: "Source Sans 3", sans-serif; color: var(--ink); position: relative; }

  .sheet { position: absolute; background: var(--paper); box-shadow: var(--shadow); }
  .brand-name { font-family: "Noto Serif", serif; font-weight: 400; color: var(--navy); white-space: nowrap; position: absolute; }

  .contact-block { position: absolute; display: flex; flex-direction: column; align-items: flex-end; }
  .contact-row { display: flex; align-items: center; justify-content: flex-end; white-space: nowrap; }
  .contact-row span { text-align: right; }
  .contact-icon { background: var(--navy); display: flex; align-items: center; justify-content: center; border-radius: 2px; flex: none; }
  .contact-icon svg { fill: none; stroke: #fff; }

  .address { position: absolute; font-style: normal; white-space: nowrap; }

  /* Letterhead */
  .letterhead { left: 14px; top: 142px; width: 593px; height: 906px; }
  .letterhead .brand-name { left: 0; right: 0; top: 80px; text-align: center; font-size: 27px; }
  .letterhead .address { left: 34px; top: 840px; font-size: 8px; line-height: 16px; }
  .letterhead .contact-block { right: 0; top: 808px; }
  .letterhead .contact-row { height: 18px; margin-bottom: 1px; font-size: 8px; gap: 12px; }
  .letterhead .contact-icon { width: 24px; height: 18px; }

  /* Envelope */
  .envelope { left: 621px; top: 222px; width: 525px; height: 248px; }
  .envelope-flap { position: absolute; left: 621px; top: 152px; width: 525px; height: 71px; }
  .envelope .brand-name { left: 8px; top: 42px; font-size: 16px; }
  .envelope .address { left: 8px; top: 210px; font-size: 7.5px; line-height: 11px; }
  .envelope .contact-block { right: 0; top: 175px; }
  .envelope .contact-row { height: 15px; margin-bottom: 1px; font-size: 7.5px; gap: 6px; }
  .envelope .contact-icon { width: 19px; height: 15px; }

  /* Business card front */
  .card-front { left: 640px; top: 526px; width: 378px; height: 220px; }
  .card-front .brand-name { left: 0; right: 0; top: 42px; text-align: center; font-size: 20px; }
  .holder { position: absolute; left: 12px; top: 119px; }
  .holder-name { font-size: 11px; font-weight: 600; color: var(--navy); line-height: 14px; }
  .holder-title { font-size: 10px; line-height: 14px; }
  .card-front .address { left: 12px; top: 160px; font-size: 10px; line-height: 16px; }
  .card-front .contact-block { right: 0; top: 114px; }
  .card-front .contact-row { height: 23px; margin-bottom: 1px; font-size: 10px; gap: 6px; }
  .card-front .contact-icon { width: 24px; height: 23px; }

  /* Business card back */
  .card-back { left: 640px; top: 773px; width: 378px; height: 221px; background: var(--navy); }
  .card-back .brand-name { left: 0; right: 0; top: 96px; text-align: center; font-size: 18px; color: var(--mist); }
</style>
</head>
<body>
<svg width="0" height="0" style="position:absolute">
  <defs>
    <symbol id="icon-phone" viewBox="0 0 12 12"><circle cx="6" cy="6" r="5"/><path d="M4 3.5l1 1.5-.6.7a4 4 0 0 0 1.9 1.9l.7-.6 1.5 1-.5 1.1c-2.6-.3-4.6-2.3-4.9-4.9z"/></symbol>
    <symbol id="icon-fax" viewBox="0 0 12 12"><rect x="2" y="3" width="3" height="7"/><rect x="5" y="5" width="5" height="5"/><path d="M5.5 5V2h3.5v3"/></symbol>
    <symbol id="icon-mail" viewBox="0 0 12 12"><rect x="1.5" y="3" width="9" height="6"/><path d="M1.5 3l4.5 3.5L10.5 3"/></symbol>
    <symbol id="icon-web" viewBox="0 0 12 12"><circle cx="6" cy="6" r="4.5"/><path d="M1.5 6h9M6 1.5c-2 2.5-2 6.5 0 9M6 1.5c2 2.5 2 6.5 0 9"/></symbol>
  </defs>
</svg>

<section class="sheet letterhead">
  <div class="brand-name">Harborline Financial</div>
  <address class="address">Bramcote Commerce Court, 781 Ashgrove Street<br>Ashbury, CT 06287</address>
  <div class="contact-block">
    <div class="contact-row"><span>203-555-0147</span><div class="contact-icon"><svg width="12" height="12"><use href="#icon-phone"/></svg></div></div>
    <div class="contact-row"><span>203-555-0162</span><div class="contact-icon"><svg width="12" height="12"><use href="#icon-fax"/></svg></div></div>
    <div class="contact-row"><span>DAshford@HarborlineFinancial.com</span><div class="contact-icon"><svg width="12" height="12"><use href="#icon-mail"/></svg></div></div>
    <div class="contact-row"><span>www.HarborlineFinancial.com</span><div class="contact-icon"><svg width="12" height="12"><use href="#icon-web"/></svg></div></div>
  </div>
</section>

<svg class="envelope-flap" viewBox="0 0 525 71" aria-hidden="true">
  <path d="M0 71 L0 20 Q0 4 18 3 L490 0 Q514 0 520 20 L525 71 Z" fill="#0f203f"/>
</svg>
<section class="sheet envelope">
  <div class="brand-name">Harborline Financial</div>
  <address class="address">Bramcote Commerce Court, 781 Ashgrove Street<br>Ashbury, CT 06287</address>
  <div class="contact-block">
    <div class="contact-row"><span>203-555-0147</span><div class="contact-icon"><svg width="10" height="10"><use href="#icon-phone"/></svg></div></div>
    <div class="contact-row"><span>203-555-0162</span><div class="contact-icon"><svg width="10" height="10"><use href="#icon-fax"/></svg></div></div>
    <div class="contact-row"><span>DAshford@HarborlineFinancial.com</span><div class="contact-icon"><svg width="10" height="10"><use href="#icon-mail"/></svg></div></div>
    <div class="contact-row"><span>www.HarborlineFinancial.com</span><div class="contact-icon"><svg width="10" height="10"><use href="#icon-web"/></svg></div></div>
  </div>
</section>

<section class="sheet card-front">
  <div class="brand-name">Harborline Financial</div>
  <div class="holder">
    <div class="holder-name">Daniel R. Ashford, Sr.RFC</div>
    <div class="holder-title">President/CEO</div>
  </div>
  <address class="address">Bramcote Commerce Court<br>781 Ashgrove Street<br>Ashbury, CT 06287</address>
  <div class="contact-block">
    <div class="contact-row"><span>203-555-0147</span><div class="contact-icon"><svg width="13" height="13"><use href="#icon-phone"/></svg></div></div>
    <div class="contact-row"><span>203-555-0162</span><div class="contact-icon"><svg width="13" height="13"><use href="#icon-fax"/></svg></div></div>
    <div class="contact-row"><span>DAshford@HarborlineFinancial.com</span><div class="contact-icon"><svg width="13" height="13"><use href="#icon-mail"/></svg></div></div>
    <div class="contact-row"><span>www.HarborlineFinancial.com</span><div class="contact-icon"><svg width="13" height="13"><use href="#icon-web"/></svg></div></div>
  </div>
</section>

<section class="sheet card-back">
  <div class="brand-name">Harborline Financial</div>
</section>
</body>
</html>
```